Harborline Talent IT Recruiting firm needs a business card design for Recruiters, Sourcers, and Account

We need business cards that allow us to change all contact info, names, titles (Recruiter, Sourcer, Account Manager, Director, CEO, etc) per person since we have three offices, in three cities, Phoenix, Austin, and Las Vegas. We do recruiting and contractors for IT positions (Developers, Architects, Software Engineers, Security Engineers, Help Desk, DBAs, PMs, Scrum Masters, etc.) Our client companies are very diverse from Crestline 250 to silicone Valley type start-ups.

So, while we what hip, techie, and quirky, it still needs to be professional. Primary color we use is blue, with silver as a secondary color.

Target Market(s)

IT, Technology

Industry/Entity Type

Business

Contact Information for Business Card

Company name: Harborline Talent, Inc.
Website: www.harborlinetalent-example.com
Logos for ProCircle, Quillo, and Roomwall

Name, Title, Office Number, Cell Number, email

Font styles to use
Serif
Sans Serif

Colors
0455a3
d5d5d5

Requirements
Nice to have
• The grey I selected below is not necessary - but, would like silver included. I included a card design (File 3: HTI early trial example.jpg) that I had started on. It's very rough, and not quite what we're looking for, but what we did like is the logo, big, maybe a bit faded, off center, goes out of frame, etc. Still looking for other ideas - you are the pros! But, just an idea of a design element we liked.

```html
<!DOCTYPE html>
<html lang="en">
<head>
<meta charset="utf-8">
<title>Harborline Talent – Business Card</title>
<link rel="stylesheet" href="https://fonts.googleapis.com/css2?family=Alegreya:wght@400;500&family=Alegreya+Sans:wght@400&display=swap">
<style>
  :root {
    --stage-top: #0c0c0c;
    --stage-mid: #8a8a8a;
    --card-light: #fbfbfb;
    --card-shade: #e4e5e7;
    --ink: #161616;
    --silver: #8e9196;
    --brand-blue: #0455a3;
    --wave-deep: #1f6f95;
    --wave-mid: #2ea0c4;
    --wave-light: #7fd0e6;
    --icon-blue: #3b86d6;
  }
  * { margin: 0; padding: 0; box-sizing: border-box; }
  html, body { width: 1200px; height: 1000px; overflow: hidden; }
  body {
    background: linear-gradient(90deg, var(--stage-top) 0%, var(--stage-mid) 50%, var(--stage-top) 100%);
    position: relative;
    font-family: "Alegreya Sans", sans-serif;
  }
  .card {
    position: absolute;
    left: 191px;
    width: 817px;
    height: 473px;
    overflow: hidden;
    background: radial-gradient(ellipse at 60% 40%, var(--card-light) 0%, var(--card-shade) 100%);
  }
  .card--front { top: 20px; }
  .card--back { top: 507px; }
  .wave { position: absolute; left: 0; top: 0; width: 817px; height: 473px; }

  .wordmark {
    position: absolute;
    font-family: "Alegreya", serif;
    font-weight: 500;
    color: var(--silver);
    text-transform: uppercase;
    line-height: 1;
    display: flex;
    align-items: center;
  }
  .wordmark__mark { border-radius: 50%; background: var(--brand-blue); flex: none; }
  .wordmark__lines { display: flex; flex-direction: column; align-items: flex-end; }

  .wordmark--large { left: 300px; top: 80px; font-size: 54px; gap: 18px; }
  .wordmark--large .wordmark__mark { width: 64px; height: 64px; }
  .wordmark--large .wordmark__lines { gap: 6px; }

  .wordmark--small { left: 600px; top: 68px; font-size: 21px; gap: 8px; }
  .wordmark--small .wordmark__mark { width: 24px; height: 24px; }
  .wordmark--small .wordmark__lines { gap: 2px; }

  .person__name {
    position: absolute; left: 62px; top: 62px;
    font-family: "Alegreya", serif; font-weight: 400;
    font-size: 62px; color: var(--ink); line-height: 1;
  }
  .person__title {
    position: absolute; left: 127px; top: 127px;
    font-family: "Alegreya", serif; font-weight: 400;
    font-size: 32px; color: var(--ink); line-height: 1;
  }
  .contact { position: absolute; font-size: 20px; color: #222; display: flex; align-items: center; gap: 13px; line-height: 1; }
  .contact svg { width: 25px; height: 25px; flex: none; }
</style>
</head>
<body>
  <svg width="0" height="0" style="position:absolute">
    <defs>
      <linearGradient id="waveFill" x1="0" y1="0" x2="1" y2="0">
        <stop offset="0" stop-color="var(--wave-deep)"/>
        <stop offset="0.5" stop-color="var(--wave-mid)"/>
        <stop offset="1" stop-color="var(--wave-light)" stop-opacity="0.5"/>
      </linearGradient>
      <radialGradient id="iconBall" cx="0.4" cy="0.35" r="0.7">
        <stop offset="0" stop-color="#a9d2f5"/>
        <stop offset="1" stop-color="var(--icon-blue)"/>
      </radialGradient>
      <symbol id="icon-phone" viewBox="0 0 25 25">
        <circle cx="12.5" cy="12.5" r="12" fill="url(#iconBall)"/>
        <path d="M9 7 q-2 6 4 11 l2 -1.5 q-2 -3 -3.5 -2 q-2 -2 -1.5 -5 q1.5 -.5 0 -3 Z" fill="#fff"/>
      </symbol>
      <symbol id="icon-mail" viewBox="0 0 25 25">
        <circle cx="12.5" cy="12.5" r="12" fill="url(#iconBall)"/>
        <rect x="6.5" y="8.5" width="12" height="8" fill="#fff"/>
        <path d="M6.5 8.5 L12.5 13 L18.5 8.5" fill="none" stroke="var(--icon-blue)" stroke-width="1.2"/>
      </symbol>
      <symbol id="icon-square" viewBox="0 0 25 25">
        <rect x="1" y="1" width="23" height="23" rx="3" fill="var(--brand-blue)"/>
      </symbol>
    </defs>
  </svg>

  <section class="card card--front">
    <svg class="wave" viewBox="0 0 817 473" role="img" aria-label="Abstract blue wave of layered translucent bands">
      <path d="M0 180 C120 220 260 295 400 318 C500 334 560 332 580 348 C500 398 420 430 300 420 C180 410 80 392 0 372 Z" fill="url(#waveFill)"/>
    </svg>
    <div class="wordmark wordmark--large">
      <span class="wordmark__mark"></span>
      <span class="wordmark__lines"><span>Harborline</span><span>Talent</span></span>
    </div>
  </section>

  <section class="card card--back">
    <svg class="wave" viewBox="0 0 817 473" role="img" aria-label="Abstract blue wave of layered translucent bands">
      <path transform="translate(817,-10) scale(-1,1)" d="M0 180 C120 220 260 295 400 318 C500 334 560 332 580 348 C500 398 420 430 300 420 C180 410 80 392 0 372 Z" fill="url(#waveFill)"/>
    </svg>
    <div class="wordmark wordmark--small">
      <span class="wordmark__mark"></span>
      <span class="wordmark__lines"><span>Harborline</span><span>Talent</span></span>
    </div>
    <h1 class="person__name">Marisol Avery</h1>
    <p class="person__title">First Touch Ambassador</p>

    <p class="contact" style="left:46px;top:272px"><svg><use href="#icon-phone"/></svg>512-555-0148</p>
    <p class="contact" style="left:316px;top:269px"><svg><use href="#icon-phone"/></svg>512-555-0193</p>
    <p class="contact" style="left:46px;top:309px"><svg><use href="#icon-mail"/></svg>marisol@harborlinetalent-example.com</p>
    <p class="contact" style="left:46px;top:345px"><svg><use href="#icon-square"/></svg>@Marisolavery</p>
    <p class="contact" style="left:46px;top:377px"><svg><use href="#icon-square"/></svg>procircle.example/marisol</p>
    <p class="contact" style="left:46px;top:408px"><svg><use href="#icon-square"/></svg>roomwall.example/marisol</p>
  </section>
</body>
</html>
```